Commercial facility maintenance

I need a card design that helps my salesmen make contact with new clients, our product is facility maintenance and heavy industrial maintenance

```html
<!DOCTYPE html>
<html lang="en">
<head>
<meta charset="UTF-8">
<title>Harlow Millwrights LLC – Business Card</title>
<link rel="stylesheet" href="https://fonts.googleapis.com/css2?family=Libre+Baskerville:wght@700&family=Open+Sans:wght@400;600;700&display=swap">
<style>
  :root {
    --backdrop: #3a3b3e;
    --card-dark: #24262d;
    --card-light: #f4f3f1;
    --brand-red: #a3192a;
    --ink: #2b2d33;
    --white: #ffffff;
  }
  * { box-sizing: border-box; margin: 0; padding: 0; }
  html, body { width: 1200px; height: 800px; overflow: hidden; }
  body {
    background: var(--backdrop);
    font-family: "Open Sans", Arial, sans-serif;
    position: relative;
  }
  .card {
    position: absolute;
    width: 600px;
    height: 343px;
    border-radius: 4px;
    overflow: hidden;
    box-shadow: 0 14px 30px rgba(0,0,0,.45);
  }

  /* Front */
  .card-front {
    left: 90px; top: 70px;
    background: var(--card-dark);
  }
  .brand-mark {
    position: absolute;
    display: flex; align-items: center; gap: 14px;
  }
  .brand-dot {
    width: 34px; height: 34px; border-radius: 50%;
    background: var(--brand-red);
    flex: none;
  }
  .brand-name {
    font-family: "Open Sans", Arial, sans-serif;
    font-weight: 700;
    color: var(--white);
    letter-spacing: .04em;
    text-transform: uppercase;
    line-height: 1.15;
  }
  .card-front .brand-mark { left: 50%; top: 132px; transform: translateX(-50%); }
  .card-front .brand-name { font-size: 30px; white-space: nowrap; }
  .front-rule {
    position: absolute; left: 110px; right: 30px; bottom: 62px;
    height: 3px; background: var(--brand-red);
  }

  /* Back */
  .card-back {
    left: 510px; top: 400px;
    display: grid;
    grid-template-columns: 230px 370px;
    background: var(--card-light);
  }
  .back-brand {
    position: relative;
    background: var(--card-dark);
  }
  .back-brand .brand-mark {
    left: 0; right: 0; top: 78px;
    justify-content: center;
    gap: 10px;
  }
  .back-brand .brand-dot { width: 22px; height: 22px; }
  .back-brand .brand-name { font-size: 15px; letter-spacing: .03em; }
  .back-wordmark {
    position: absolute; left: 0; right: 0; top: 236px;
    text-align: center;
    font-family: "Libre Baskerville", Georgia, serif;
    font-weight: 700;
    color: var(--white);
  }
  .back-wordmark .line-1 { display: block; font-size: 27px; letter-spacing: .02em; }
  .back-wordmark .line-2 { display: block; font-size: 12px; letter-spacing: .18em; margin-top: 2px; }
  .back-rule {
    position: absolute; left: 0; right: 0; bottom: 24px;
    height: 4px; background: var(--brand-red);
  }

  .back-info {
    position: relative;
    padding: 26px 20px 0 30px;
    color: var(--ink);
  }
  .services {
    border-left: 2px solid var(--brand-red);
    padding-left: 16px;
    height: 270px;
  }
  .section-title {
    color: var(--brand-red);
    font-weight: 700;
    font-size: 19px;
    letter-spacing: .03em;
    text-transform: uppercase;
    margin-bottom: 8px;
  }
  .service-list { list-style: none; }
  .service-list li {
    position: relative;
    padding-left: 14px;
    font-size: 15px;
    line-height: 1.28;
    margin-bottom: 6px;
  }
  .service-list li::before {
    content: "";
    position: absolute; left: 0; top: 8px;
    width: 5px; height: 5px; border-radius: 50%;
    background: var(--brand-red);
  }
  .contact {
    position: absolute;
    left: 165px; top: 188px;
    border-left: 2px solid var(--brand-red);
    padding-left: 14px;
    height: 130px;
  }
  .contact .section-title { font-size: 18px; margin-bottom: 6px; }
  .contact p { font-size: 15px; line-height: 1.6; white-space: nowrap; }
  .contact .web { font-size: 12.5px; margin-top: 4px; }
</style>
</head>
<body>

  <section class="card card-front" aria-label="Business card front">
    <div class="brand-mark">
      <span class="brand-dot"></span>
      <span class="brand-name">Harlow Millwrights LLC</span>
    </div>
    <div class="front-rule"></div>
  </section>

  <section class="card card-back" aria-label="Business card back">
    <div class="back-brand">
      <div class="brand-mark">
        <span class="brand-dot"></span>
        <span class="brand-name">Harlow<br>Millwrights LLC</span>
      </div>
      <div class="back-wordmark">
        <span class="line-1">HARLOW</span>
        <span class="line-2">MILLWRIGHTS LLC</span>
      </div>
      <div class="back-rule"></div>
    </div>

    <div class="back-info">
      <div class="services">
        <h2 class="section-title">Our Services</h2>
        <ul class="service-list">
          <li>Welding and Demolition</li>
          <li>Operation and Maintenance<br>of Industial Machinery</li>
          <li>Setting, Moving &amp; Installation of<br>Industrial Machinery</li>
        </ul>
      </div>
      <div class="contact">
        <h2 class="section-title">Contact</h2>
        <p>555-014-2287</p>
        <p>crew@harlowmw.com</p>
        <p class="web">harlowmillwrightsllc.com</p>
      </div>
    </div>
  </section>

</body>
</html>
```